Vorbanix Stationery Design Project

We need a stationery design for our new business Vorbanix which deals in Precision Surface Care Systems such as Ultrasonic cleaning and high pressure cleaning machinery.

Our colour scheme is as per the included files.

We require business cards, letterheads, a brochure folder and email signatures design
Updates

Project Deadline Extended

Apologies for the delay in making a decision on this project. We will be making a final decision during the course of next week

Target Market(s)

Industries ranging from medical, automotive, mining, engineering all requiring specialised cleaning services

Industry/Entity Type

Pressure Cleaning

Requirements
Must have
• Please include our supplied logo and colour scheme. The design needs to be professional but creative.

```html
<!DOCTYPE html>
<html lang="en">
<head>
<meta charset="utf-8">
<title>Vorbanix Stationery</title>
<link href="https://fonts.googleapis.com/css2?family=Open+Sans:wght@400;600;700&display=swap" rel="stylesheet">
<style>
  :root {
    --blue: #2b3d8f;
    --blue-deep: #1f2c6e;
    --blue-light: #4660b8;
    --silver: #c9ccd3;
    --grey-text: #8a8d93;
    --ink: #4a4d55;
    --paper: #ffffff;
    --backdrop: #e4e5e8;
  }
  * { box-sizing: border-box; margin: 0; padding: 0; }
  html, body { width: 1200px; height: 782px; overflow: hidden; }
  body {
    background: var(--backdrop);
    font-family: "Open Sans", Arial, sans-serif;
    color: var(--ink);
    position: relative;
  }
  .sheet { position: absolute; background: var(--paper); overflow: hidden; box-shadow: 0 2px 8px rgba(0,0,0,.12); }

  .brand { display: flex; align-items: center; gap: 7px; }
  .brand-dot { width: 16px; height: 16px; background: var(--blue); flex: none; }
  .brand-name { font-weight: 700; color: var(--grey-text); font-size: 17px; letter-spacing: .5px; line-height: 1; }
  .brand-tag { font-size: 7px; color: var(--grey-text); margin-top: 3px; margin-left: 23px; white-space: nowrap; }

  .contact { display: flex; gap: 12px; font-size: 6.5px; line-height: 1.5; color: var(--grey-text); white-space: nowrap; }
  .contact strong { font-weight: 700; color: var(--ink); display: block; }
  .contact-lines span { display: flex; align-items: center; gap: 3px; }
  .ico { width: 5px; height: 5px; border-radius: 50%; background: var(--blue); display: inline-block; flex: none; }

  .footer-band { position: absolute; left: 0; right: 0; bottom: 0; height: 14px; background: var(--blue); }
  .footer-rule { position: absolute; left: 0; right: 0; bottom: 18px; height: 3px; background: var(--silver); }

  /* Letterhead */
  .letterhead { left: 40px; top: 94px; width: 420px; height: 594px; }
  .letterhead .brand-block { position: absolute; left: 34px; top: 40px; }
  .letterhead .contact { position: absolute; right: 30px; top: 40px; }

  /* Envelope */
  .envelope { left: 510px; top: 60px; width: 620px; height: 300px; }
  .envelope .top-band { position: absolute; left: 0; top: 0; right: 0; height: 70px; background: var(--blue); }
  .envelope .top-rule { position: absolute; left: 0; right: 0; top: 74px; height: 3px; background: var(--silver); }
  .envelope .brand-block { position: absolute; left: 34px; top: 150px; }
  .envelope .window {
    position: absolute; left: 46px; top: 205px; width: 230px; height: 62px;
    border: 1px solid #dcdde0; border-radius: 10px; background: #f4f4f6;
  }

  /* Business cards */
  .card { width: 300px; height: 172px; }
  .card-front { left: 510px; top: 420px; }
  .card-front .name-band {
    position: absolute; left: 0; right: 0; top: 30px; height: 24px; background: var(--blue);
    display: flex; align-items: center; padding-left: 16px;
    color: #fff; font-size: 9px; font-weight: 700;
  }
  .card-front .name-band span { font-weight: 400; opacity: .85; margin-left: 4px; border-left: 1px solid rgba(255,255,255,.6); padding-left: 4px; }
  .card-front .brand-block { position: absolute; left: 18px; top: 116px; }
  .card-front .contact { position: absolute; left: 186px; top: 76px; flex-direction: column; gap: 4px; }

  .card-back { left: 830px; top: 420px; background: linear-gradient(135deg, var(--blue-light), var(--blue-deep)); }
  .card-back .back-rule { position: absolute; left: 0; right: 0; bottom: 24px; height: 3px; background: var(--silver); }
  .card-back .url {
    position: absolute; left: 14px; top: 100px; transform: rotate(-90deg); transform-origin: left top;
    font-size: 7px; color: rgba(255,255,255,.8); letter-spacing: .4px; white-space: nowrap;
  }
</style>
</head>
<body>

<section class="sheet letterhead">
  <div class="brand-block">
    <div class="brand"><span class="brand-dot"></span><span class="brand-name">VORBANIX</span></div>
    <div class="brand-tag">Precision Surface Care Systems</div>
  </div>
  <div class="contact">
    <div><strong>48 Harbor Lane</strong><strong>Suite 210</strong><strong>Riverton CA 90210</strong></div>
    <div class="contact-lines">
      <span><i class="ico"></i>(555) 204-3817</span>
      <span><i class="ico"></i>(555) 204-3818</span>
      <span><i class="ico"></i>vorbanix.com</span>
    </div>
  </div>
  <div class="footer-rule"></div>
  <div class="footer-band"></div>
</section>

<section class="sheet envelope">
  <div class="top-band"></div>
  <div class="top-rule"></div>
  <div class="brand-block">
    <div class="brand"><span class="brand-dot"></span><span class="brand-name">VORBANIX</span></div>
    <div class="brand-tag">Precision Surface Care Systems</div>
  </div>
  <div class="window"></div>
  <div class="footer-band"></div>
</section>

<section class="sheet card card-front">
  <div class="name-band">Lena Marsh<span>Position</span></div>
  <div class="brand-block">
    <div class="brand"><span class="brand-dot"></span><span class="brand-name">VORBANIX</span></div>
    <div class="brand-tag">Precision Surface Care Systems</div>
  </div>
  <div class="contact">
    <div><strong>48 Harbor Lane</strong><strong>Suite 210</strong><strong>Riverton CA 90210</strong></div>
    <div class="contact-lines">
      <span><i class="ico"></i>(555) 204-3817</span>
      <span><i class="ico"></i>(555) 204-3818</span>
      <span><i class="ico"></i>vorbanix.com</span>
    </div>
  </div>
</section>

<section class="sheet card card-back">
  <div class="back-rule"></div>
  <div class="url">www.vorbanix.com</div>
</section>

</body>
</html>
```